Website for company called VORENTbio

We need a website for our new company called VORENTbio which developed a platform/technology to identify antigen-specific T cells (immune cells) which can be used for cancer therapy, autoimmunity, etc.

The platform is called VORENT and is rapid, versatile, unbiased, and inexpensive.

We have a semi-final logo although we are not completely set on color and font of text (attached).

Target Market(s)

Our target audience at the moment would be potential investors and VCs. We eventually are interested in getting attention from scientists and cell/immunotherapy companies.

Industry/Entity Type

Healthcare/Technology

Coding

Coded - Design and coding required

Number of Pages Required

1 page

Colors
0094D4
00A9DD
6FCCEA
C7EBF8
E9F6FB
00AB8E
00BBA5
67D7C9
C6EFE9
E9F9F6
E54698
E96AAD
F1A4CE
F9D9EA
FCEFF6
A7469A
B969AE
D3A5CF
EDDBEB
F8F0F9
6B429C
8869AF
B7A5CE
E3DAEB
F3F0F8

Requirements
Must have
• Landing page about the company, About us page, Technology page (could be merged with company landing page), Contact us page

```html
<!DOCTYPE html>
<html lang="en">
<head>
<meta charset="utf-8">
<title>VORENTbio — Advancing immune cell discovery</title>
<link rel="stylesheet" href="https://fonts.googleapis.com/css2?family=Inter+Tight:ital,wght@0,400;0,500;0,600;1,500&display=swap">
<style>
:root{
  --ink:#111318;
  --muted:#6b6f7a;
  --line:#e6e8ee;
  --navy:#0d1b6e;
  --dark:#1b1b1d;
  --dark-line:#34353a;
  --white:#ffffff;
  --pink:#e96aad;
  --violet:#b7a5ce;
}
*{box-sizing:border-box;margin:0;padding:0}
html,body{width:1200px;height:5182px;overflow:hidden;background:var(--white)}
body{position:relative;font-family:"Inter Tight",Arial,sans-serif;color:var(--ink)}
.abs{position:absolute}
.photo{position:absolute;border-radius:10px}
.logo{display:flex;align-items:center;gap:8px;font-weight:600;font-size:19px;letter-spacing:-.3px}
.logo .mark{width:14px;height:14px;background:currentColor;border-radius:3px}
.btn{position:absolute;display:flex;align-items:center;justify-content:center;gap:10px;font-size:11px;font-weight:500;border-radius:3px;text-decoration:none}
.btn-dark{background:var(--navy);color:var(--white)}
.btn-line{border:1px solid var(--line);color:var(--ink);background:var(--white)}
.btn .sep{width:1px;height:12px;background:rgba(255,255,255,.4)}
h1,h2,h3{font-weight:500;letter-spacing:-.04em}
.section-title{position:absolute;left:0;width:1200px;text-align:center;font-size:28px}
.lede{position:absolute;text-align:center;font-size:11.5px;line-height:18px;color:var(--muted)}
.small{font-size:11px;line-height:17px;color:var(--muted)}
.feature{position:absolute;top:720px;width:214px;height:240px;border-left:1px solid var(--line);padding:30px 20px}
.feature::before{content:"";position:absolute;left:-3px;top:-2px;width:5px;height:5px;border-radius:50%;background:#cfd3dc}
.feature .icon{width:34px;height:34px;border-radius:8px}
.feature h3{font-size:13.5px;letter-spacing:-.01em;margin-top:48px}
.feature p{margin-top:12px}
.tabs{position:absolute;left:170px;top:1802px;display:flex;gap:26px;font-size:11px;color:#a4a8b2}
.tabs .on{color:var(--ink);font-weight:500;border-bottom:2px solid var(--navy);padding-bottom:5px}
.sci{position:absolute;display:flex;align-items:center;gap:10px}
.sci .av{width:34px;height:34px;border-radius:50%;background:linear-gradient(135deg,#d9d4cf,#9a948e)}
.sci b{display:block;font-size:10.5px;font-weight:500}
.sci span{font-size:9px;color:var(--muted)}
.stream{position:absolute;left:150px;top:2244px;width:894px;height:368px;border:1px solid #d9ddea;border-radius:14px;background:linear-gradient(180deg,#fff,#f3f4fa)}
.option{position:absolute;left:478px;width:396px;height:38px;background:var(--white);border:1px solid var(--line);border-radius:6px;display:flex;align-items:center;gap:10px;padding-left:14px;font-size:11px}
.option svg{width:14px;height:14px}
.events{position:absolute;left:150px;top:3092px;width:894px;height:888px;background:var(--dark);border-radius:14px;color:var(--white);overflow:hidden}
.events h2{position:absolute;left:132px;top:62px;font-size:28px}
.events .rule{position:absolute;left:0;width:894px;height:1px;background:var(--dark-line)}
.pill{position:absolute;height:24px;padding:0 14px;border:1px solid #8a8b90;border-radius:12px;background:var(--dark);font-size:9.5px;display:flex;align-items:center}
.event-title{position:absolute;width:250px;font-size:15px;line-height:26px;font-weight:500;letter-spacing:-.02em}
.card{position:absolute;left:220px;width:752px;background:var(--white);border:1px solid var(--line);border-radius:6px;box-shadow:0 -6px 18px rgba(0,0,0,.05);overflow:hidden}
.card .ttl{position:absolute;left:38px;top:20px;display:flex;align-items:center;gap:12px;font-size:20px;letter-spacing:-.03em}
.card .ttl i{width:28px;height:28px;border-radius:6px;background:linear-gradient(135deg,#f1a4ce,#b7a5ce)}
.footer{position:absolute;left:150px;top:4752px;width:894px;height:350px;background:var(--dark);border-radius:14px;color:var(--white)}
.fnav{position:absolute;left:476px;top:28px;width:286px;height:116px;border:1px solid #55565b;border-radius:6px}
.fcol{position:absolute;top:10px;font-size:9px;line-height:20px;color:#d8d8dc}
.fcol b{display:block;color:var(--white);font-weight:600;margin-bottom:6px}
</style>
</head>
<body>

<header>
  <div class="logo abs" style="left:26px;top:100px"><span class="mark"></span>VORENTbio</div>
  <a class="btn btn-dark" style="left:1004px;top:98px;width:124px;height:28px">Schedule a Call
    <svg width="11" height="11" viewBox="0 0 12 12" fill="none" stroke="#fff" stroke-width="1.2"><rect x="1.5" y="2.5" width="9" height="8" rx="1"/><path d="M1.5 5h9M4 1v3M8 1v3"/></svg>
  </a>
  <svg class="abs" style="left:1148px;top:104px" width="18" height="14" viewBox="0 0 18 14" fill="none" stroke="#0d1b6e" stroke-width="1.5"><path d="M1 2h16M1 7h11M1 12h16"/></svg>
</header>

<section>
  <div class="photo" role="img" aria-label="Hero illustration of immune cells" style="left:570px;top:220px;width:170px;height:196px;border-radius:12px;background:linear-gradient(180deg,#f4f4f6,#e4e4e8)"></div>
  <span class="abs" style="left:1170px;top:366px;width:16px;height:16px;border-radius:50%;background:var(--ink)"></span>
  <div class="abs" style="left:170px;top:450px;height:22px;padding:0 10px;border:1px solid var(--line);border-radius:4px;font-size:10px;display:flex;align-items:center;gap:6px;color:#444">+ Immunotherapy Platform</div>
  <h1 class="abs" style="left:168px;top:488px;font-size:44px;line-height:54px;font-style:italic;letter-spacing:-.06em">Advancing immune cell<br>discovery for better therapies.</h1>
  <a class="btn btn-dark" style="left:170px;top:608px;width:128px;height:34px">Learn More <span class="sep"></span>→</a>
  <a class="btn btn-line" style="left:306px;top:608px;width:98px;height:34px">Contact Us</a>
</section>

<section>
  <div class="feature" style="left:170px"><div class="icon" style="background:linear-gradient(135deg,#f9d9ea,#b7a5ce)"></div><h3>Rapid</h3><p class="small">Find antigen-specific T cells in days, not months of screening.</p></div>
  <div class="feature" style="left:384px"><div class="icon" style="background:linear-gradient(135deg,#fcEff6,#f1a4ce)"></div><h3>Versatile</h3><p class="small">One platform for cancer, autoimmunity and infectious disease.</p></div>
  <div class="feature" style="left:598px"><div class="icon" style="background:linear-gradient(135deg,#f1a4ce,#d3a5cf)"></div><h3>Unbiased</h3><p class="small">Reads every T cell response without pre-selected antigen panels.</p></div>
  <div class="feature" style="left:812px"><div class="icon" style="background:linear-gradient(135deg,#e3daeb,#8869af)"></div><h3>Inexpensive</h3><p class="small">Standard lab equipment keeps each run affordable at scale.</p></div>
  <div class="abs" style="left:170px;top:960px;width:856px;height:1px;background:var(--line)"></div>
</section>

<section>
  <h2 class="section-title" style="top:1060px">The Team Behind VORENT</h2>
  <p class="lede" style="left:390px;top:1110px;width:420px">Each scientist brings a unique set of skills and passion, united by a shared commitment to turning T cell discovery into better therapies.</p>
  <div class="photo" role="img" aria-label="Portrait of a scientist" style="left:274px;top:1205px;width:56px;height:400px;background:linear-gradient(180deg,#e9e6e1,#b9b3ad)"></div>
  <div class="photo" role="img" aria-label="Portrait of the chief scientific officer" style="left:342px;top:1205px;width:374px;height:400px;background:linear-gradient(160deg,#4e4b5c,#8c8a99 55%,#e8e8ee)">
    <div class="abs" style="left:26px;top:30px;font-size:7.5px;letter-spacing:.08em;color:#b7a5ce">CHIEF SCIENTIFIC OFFICER</div>
    <div class="abs" style="left:26px;top:44px;font-size:17px;color:#fff;font-weight:500">Owen Marlow</div>
  </div>
  <div class="photo" role="img" aria-label="Portrait of a scientist" style="left:726px;top:1205px;width:58px;height:400px;background:linear-gradient(180deg,#a9cde6,#e7c79f 50%,#5f8fc0)"></div>
  <div class="photo" role="img" aria-label="Portrait of a scientist" style="left:796px;top:1205px;width:56px;height:400px;background:linear-gradient(180deg,#c9dff0,#e7d0c3 50%,#6c88b0)"></div>
  <div class="photo" role="img" aria-label="Portrait of a scientist" style="left:864px;top:1205px;width:56px;height:400px;background:linear-gradient(180deg,#b8a69c,#e6c9b7 50%,#d7d2cc)"></div>
</section>

<section>
  <div class="abs" role="img" aria-label="Soft grey background decoration" style="left:840px;top:1610px;width:360px;height:300px;background:radial-gradient(ellipse at 60% 40%,#ececec 0%,#f3f3f3 50%,transparent 70%)"></div>
  <h2 class="abs" style="left:170px;top:1726px;font-size:28px">Helping Humanity</h2>
  <nav class="tabs"><span class="on">Cancer</span><span>Autoimmunity</span><span>Infection</span><span>Vaccines</span><span>Transplant</span></nav>
  <p class="small abs" style="left:170px;top:1846px;width:330px">With VORENT, we map the T cells that recognise tumours, guiding the next wave of cell therapies.</p>
  <a class="btn btn-dark" style="left:170px;top:1924px;width:138px;height:32px">Explore More <span class="sep"></span>→</a>
  <div class="abs" style="left:170px;top:2074px;font-size:8.5px;font-weight:600;letter-spacing:.06em">KEY SCIENTISTS</div>
  <div class="sci" style="left:170px;top:2096px"><span class="av"></span><div><b>Dr. Peter Vasko</b><span>T Cell Immunologist</span></div></div>
  <div class="sci" style="left:330px;top:2096px"><span class="av"></span><div><b>Dr. Simon Aldana</b><span>Cancer Biologist</span></div></div>
  <div class="photo" role="img" aria-label="Family walking together outdoors" style="left:624px;top:1802px;width:400px;height:330px;background:linear-gradient(180deg,#6b6a52,#8a7e62 55%,#4e5a3a)"></div>
</section>

<section class="stream">
  <div class="photo" role="img" aria-label="Researcher working in a dark lab" style="left:20px;top:36px;width:396px;height:296px;background:linear-gradient(160deg,#1b2330,#3e4e5e 55%,#7fa3b8)"></div>
  <h2 class="abs" style="left:478px;top:38px;font-size:24px;line-height:30px;letter-spacing:-.03em">Screen, Identify, and Elevate<br>Your Pipeline</h2>
  <p class="small abs" style="left:478px;top:112px;width:400px">Efficient T cell discovery tailored to your program, where unbiased screening meets speed.</p>
  <div class="option" style="top:168px"><svg viewBox="0 0 14 14" fill="none" stroke="#444" stroke-width="1.1"><path d="M3 11l5-5M8 3l3 3-2 2-3-3z"/></svg>Antigen Discovery</div>
  <div class="option" style="top:222px"><svg viewBox="0 0 14 14" fill="none" stroke="#444" stroke-width="1.1"><path d="M2 3h10M7 3v9M4 7h6"/></svg>TCR Identification</div>
  <div class="option" style="top:274px"><svg viewBox="0 0 14 14" fill="none" stroke="#444" stroke-width="1.1"><circle cx="7" cy="7" r="2.5"/><path d="M7 1v2M7 11v2M1 7h2M11 7h2M3 3l1.4 1.4M9.6 9.6L11 11M3 11l1.4-1.4M9.6 4.4L11 3"/></svg>Partnered Research</div>
</section>

<section>
  <svg class="abs" style="left:170px;top:2710px" width="22" height="52" viewBox="0 0 22 52" fill="none" stroke="#999" stroke-width="1.2"><path d="M1 2h10M1 10h14M1 18h10M1 26h14M1 34h10"/><path d="M1 48h20" stroke="#111" stroke-width="2"/></svg>
  <h2 class="abs" style="left:170px;top:2850px;font-size:24px;line-height:30px;letter-spacing:-.03em">More Targets, for<br>More Patients</h2>
  <p class="small abs" style="left:170px;top:2930px;width:260px">We make T cell discovery fast and affordable, opening new therapies for many more people.</p>
  <a class="btn btn-line" style="left:170px;top:3010px;width:98px;height:32px">Contact Us</a>
  <div class="photo" role="img" aria-label="Close view of hands at work" style="left:498px;top:2712px;width:526px;height:330px;background:linear-gradient(150deg,#b58a70,#d9b49a 50%,#8a6150)"></div>
  <div class="abs" style="left:828px;top:2980px;width:180px;height:72px;border-radius:8px;background:linear-gradient(135deg,rgba(183,165,206,.85),rgba(233,106,173,.85));color:#fff;padding:12px">
    <div style="font-size:19px">87%</div>
    <div style="font-size:8.5px;margin-top:12px;font-weight:500">Faster Target Discovery</div>
  </div>
</section>

<section class="events">
  <h2>Upcoming Talks &amp; Investor Events</h2>
  <div class="rule" style="top:170px"></div>
  <div class="pill" style="left:132px;top:158px">25 Jan, 2024</div>
  <div class="event-title" style="left:132px;top:240px">Antigen-Specific T Cells in Cancer Therapy Symposium</div>
  <div class="photo" role="img" aria-label="Audience at a science talk" style="left:466px;top:198px;width:296px;height:146px;border-radius:4px;background:linear-gradient(135deg,#c9b8a8,#8c7a6e 60%,#d25a5a)"></div>

  <div class="rule" style="top:412px"></div>
  <div class="pill" style="left:466px;top:400px">25 Jan, 2024</div>
  <div class="photo" role="img" aria-label="Group seated in a workshop" style="left:132px;top:438px;width:296px;height:146px;border-radius:4px;background:linear-gradient(135deg,#d6cfc3,#8d7e6c 60%,#b9a79a)"></div>
  <div class="event-title" style="left:466px;top:480px">A Workshop on Unbiased Immune Cell Screening</div>

  <div class="rule" style="top:652px"></div>
  <div class="pill" style="left:132px;top:640px">25 Jan, 2024</div>
  <div class="event-title" style="left:132px;top:720px">Investor Day: The VORENT Platform Roadmap</div>
  <div class="photo" role="img" aria-label="Presentation in front of a whiteboard" style="left:466px;top:680px;width:296px;height:146px;border-radius:4px;background:linear-gradient(135deg,#e4e2dc,#9d9488 60%,#5a5048)"></div>
</section>

<section>
  <h2 class="section-title" style="top:4030px">Your Partner in Immune Discovery</h2>
  <p class="lede" style="left:390px;top:4080px;width:420px">We believe T cell insight should be fast and open to every lab. Our team works with scientists and therapy companies across a wide range of programs and diseases.</p>
  <div class="card" style="top:4176px;height:60px"><div class="ttl"><i></i>Cancer Therapy</div><div class="photo" style="left:466px;top:24px;width:248px;height:40px;border-radius:0;background:#3a3a3a" role="img" aria-label="Cancer research photo"></div></div>
  <div class="card" style="top:4230px;height:60px"><div class="ttl"><i></i>Autoimmunity</div><div class="photo" style="left:466px;top:24px;width:248px;height:40px;border-radius:0;background:#555" role="img" aria-label="Autoimmunity research photo"></div></div>
  <div class="card" style="top:4284px;height:388px">
    <div class="ttl"><i></i>Antigen Discovery</div>
    <p class="small abs" style="left:38px;top:196px;width:350px">With an unbiased approach, VORENT pairs each T cell with the antigen it recognises, giving clear targets for new cell therapies.</p>
    <a class="btn btn-dark" style="left:38px;top:276px;width:184px;height:32px">Book a Meeting <span class="sep"></span>→</a>
    <div class="photo" role="img" aria-label="Black and white photo of a scientist at work" style="left:466px;top:16px;width:248px;height:360px;border-radius:0;background:linear-gradient(150deg,#e8e8e8,#9a9a9a 55%,#3c3c3c)"></div>
  </div>
</section>

<footer class="footer">
  <div class="logo abs" style="left:40px;top:48px;color:#fff"><span class="mark"></span>VORENTbio</div>
  <h2 class="abs" style="left:40px;top:100px;font-size:28px;line-height:36px">Take the Next Step with<br>VORENT</h2>
  <a class="btn abs" style="left:40px;top:216px;width:124px;height:28px;background:#fff;color:var(--ink)">Schedule a Call</a>
  <div class="fnav">
    <div class="fcol" style="left:10px"><b>VORENTbio</b><u>Home</u><br>About</div>
    <div class="fcol" style="left:108px"><b>Technology</b>Cancer<br>Autoimmune<br>Infection<br>Vaccines<br>Transplant</div>
    <div class="fcol" style="left:206px"><b>Events</b>Talks<br>Investors<br>Contact</div>
  </div>
  <div class="abs" style="left:40px;top:292px;font-size:9.5px;color:#d8d8dc">VORENTbio © 2024.</div>
</footer>

</body>
</html>
```